LEAP GLOW SPIN

Need a 4 X 6 post card design. Here are the elements that need to be on the card:
LEAP, GLOW, SPIN (This is the title please feel free and create)
DATE: August 28, 2022
Showtimes 2:30 PM & 7:30 PM
Location: Harriet Colwin Theatre Linden Ridge
Tickets can be purchased at:
http://colwinstagehall.ticketnook.example/LEAPGLOWSPIN or
by calling the ticket office at (555) 555-PLAY
LEAP, GLOW, SPIN showcases the dance stylings of urban hip hop, ballet, modern jazz and much much more! Bay Area renown dancer/choreographer Rosa Jean Fairbank headlines this cast of dancers and will amaze you as she takes you on a journey through dance that you will never forget. Join us for an experience that will prove to excite and delight you!
Now for the artwork I would like to incorporate all three of these photos. The photo entitled "beach" you are only to use the dancer on the left. So clip out the other dancer in the pink dress. The Garden photo and the beach photo the images need to be cut out from the background. The sidewalk photo you can leave the background (just my preference) but for the sake of the overall design I'm ok with removing its background as well.
Ok have at it. I want to end this competition in a few days so let's get these designs in. Thank you!

```html
<!DOCTYPE html>
<html lang="en">
<head>
<meta charset="utf-8">
<title>LEAP GLOW SPIN – Postcard</title>
<link rel="stylesheet" href="https://fonts.googleapis.com/css2?family=League+Spartan:wght@600;700&family=Poppins:wght@400;500;600;700&family=Oswald:wght@500&display=swap">
<style>
  :root {
    --ink: #0b0b0b;
    --paper: #ffffff;
    --blue: #0a4ea3;
    --magenta: #d0106c;
    --gold: #f5c21b;
    --purple: #4b2579;
    --hot-pink: #f012c8;
    --grey: #d9d9d9;
    --rule: #7a7a7a;
  }
  * { box-sizing: border-box; margin: 0; padding: 0; }
  html, body { width: 1200px; height: 2766px; overflow: hidden; }
  body { background: var(--paper); position: relative; font-family: "Poppins", sans-serif; color: var(--ink); }

  .postcard { position: absolute; left: 116px; width: 968px; height: 646px; background: var(--paper); overflow: hidden; box-shadow: 0 4px 10px rgba(0,0,0,.25); }
  .postcard--front { top: 1228px; }
  .postcard--back { top: 1944px; }

  /* front */
  .hero-photo { position: absolute; left: 0; top: 0; width: 475px; height: 646px;
    background: linear-gradient(100deg, #8a8a8a 0%, #c9c9c9 22%, #f1eef4 45%, #2a2a2a 72%, #050505 100%); }
  .hero-photo::before { content: ""; position: absolute; left: 0; top: 0; width: 380px; height: 140px;
    background: linear-gradient(180deg, #6d3fa0, rgba(109,63,160,0)); }
  .front-initials { position: absolute; left: 375px; top: 30px; font-family: "League Spartan", sans-serif; font-weight: 700; font-size: 128px; line-height: 113px; }
  .front-initials span { display: block; }
  .blue { color: var(--blue); } .magenta { color: var(--magenta); } .gold { color: var(--gold); }

  .title-band { position: absolute; left: 491px; top: 38px; width: 370px; height: 93px; background: var(--ink); }
  .front-words { position: absolute; left: 494px; top: 30px; font-family: "League Spartan", sans-serif; font-weight: 700; font-size: 128px; line-height: 113px; letter-spacing: -2px; }
  .front-words span { display: block; }
  .front-words .on-band { color: var(--paper); }

  .dancer-photo { position: absolute; left: 862px; top: 0; width: 106px; height: 372px;
    background: linear-gradient(180deg, #3a3a3a, #0d0d0d 55%, #2b2b2b); border-radius: 50px 40px 20px 30px; }

  .date-day { position: absolute; left: 502px; top: 392px; font-family: "League Spartan", sans-serif; font-weight: 700; font-size: 58px; line-height: 58px; color: var(--purple); }
  .date-day sup { font-size: 30px; vertical-align: 22px; margin-left: 2px; }
  .date-month { position: absolute; left: 502px; top: 448px; font-family: "League Spartan", sans-serif; font-weight: 700; font-size: 31px; line-height: 32px; }
  .date-year { position: absolute; left: 633px; top: 394px; width: 42px; height: 85px; background: var(--ink); color: var(--paper);
    font-family: "League Spartan", sans-serif; font-weight: 700; font-size: 30px; display: flex; align-items: center; justify-content: center; }
  .date-year span { transform: rotate(-90deg); display: block; line-height: 1; padding-top: 4px; }
  .showtimes { position: absolute; left: 685px; top: 390px; font-family: "Oswald", sans-serif; font-weight: 500; font-size: 40px; line-height: 46px; color: #2a2a2a; letter-spacing: -0.5px; white-space: nowrap; transform: scaleX(0.78); transform-origin: left top; }
  .venue { position: absolute; left: 716px; top: 442px; width: 200px; height: 36px; border: 2px solid var(--ink); display: flex; align-items: center; }
  .venue-pin { width: 32px; height: 32px; background: var(--purple); display: flex; align-items: center; justify-content: center; flex: none; }
  .venue-text { font-size: 13px; line-height: 15px; color: #555; padding-left: 6px; white-space: nowrap; }

  .ticket-head { position: absolute; left: 502px; top: 488px; width: 416px; height: 23px; background: var(--magenta); color: var(--paper);
    font-size: 15px; font-weight: 500; text-align: center; line-height: 23px; }
  .ticket-url { position: absolute; left: 502px; top: 511px; width: 416px; height: 27px; background: var(--ink); color: var(--paper);
    font-size: 11px; text-align: center; line-height: 27px; white-space: nowrap; }
  .or-divider { position: absolute; left: 502px; top: 550px; width: 416px; display: flex; align-items: center; gap: 12px; font-weight: 600; font-size: 18px; }
  .or-divider::before, .or-divider::after { content: ""; flex: 1; height: 2px; background: var(--ink); }
  .call-line { position: absolute; left: 500px; top: 574px; font-size: 16.5px; white-space: nowrap; }
  .call-line .phone { font-weight: 700; margin-left: 6px; }
  .call-line svg { vertical-align: -2px; margin-left: 10px; }

  /* back */
  .back-panel { position: absolute; left: 0; top: 0; width: 475px; height: 646px; background: var(--ink); }
  .ghost-photo { position: absolute; left: 305px; top: 0; width: 170px; height: 646px;
    background: linear-gradient(90deg, rgba(40,40,40,0), #2a2a2a 60%, #1a1a1a); }
  .pink-photo { position: absolute; left: 370px; top: 80px; width: 200px; height: 566px;
    background: linear-gradient(180deg, #2d4f6a 0%, #6b4a3c 18%, var(--hot-pink) 30%, #ff3ad6 65%, var(--hot-pink) 100%);
    border-radius: 90px 90px 20px 40px; }
  .back-title { position: absolute; left: 48px; top: 46px; font-family: "League Spartan", sans-serif; font-weight: 700; font-size: 82px; line-height: 70px; color: var(--paper); letter-spacing: -1px; }
  .back-title span { display: block; }
  .back-title .initial { display: inline; }
  .blurb { position: absolute; left: 48px; top: 272px; width: 292px; color: var(--paper); font-size: 14.5px; line-height: 16.2px; }
  .back-tickets { position: absolute; left: 36px; top: 460px; width: 326px; height: 52px; border: 2px solid var(--magenta); }
  .back-tickets-head { height: 26px; background: var(--ink); color: var(--paper); font-size: 13.5px; text-align: center; line-height: 26px; }
  .back-tickets-url { height: 22px; background: var(--magenta); color: var(--paper); font-size: 9px; text-align: center; line-height: 22px; white-space: nowrap; }
  .back-call { position: absolute; left: 34px; top: 530px; color: var(--paper); font-size: 20px; font-weight: 500; }
  .back-phone { position: absolute; left: 34px; top: 560px; color: var(--paper); font-size: 27px; font-weight: 700; display: flex; align-items: center; gap: 12px; }

  .stamp-box { position: absolute; left: 819px; top: 37px; width: 96px; height: 96px; background: var(--grey); }
  .address-line { position: absolute; left: 624px; width: 293px; height: 1px; background: var(--rule); }
  .address-line--1 { top: 296px; }
  .address-line--2 { top: 341px; }
  .address-line--3 { top: 390px; }
</style>
</head>
<body>

<section class="postcard postcard--front">
  <div class="hero-photo" role="img" aria-label="Dancer in a white dress holding a flowing purple scarf overhead, faded portrait behind"></div>
  <div class="front-initials">
    <span class="blue">L</span><span class="magenta">G</span><span class="gold">S</span>
  </div>
  <div class="title-band"></div>
  <div class="front-words">
    <span class="on-band">EAP</span><span>LOW</span><span>PIN</span>
  </div>
  <div class="dancer-photo" role="img" aria-label="Dancer in black outfit balancing on one leg with arms raised"></div>

  <div class="date-day">28<sup>TH</sup></div>
  <div class="date-month">AUGUST</div>
  <div class="date-year"><span>2022</span></div>
  <div class="showtimes">2:30 PM &amp; 7:30 PM</div>
  <div class="venue">
    <div class="venue-pin">
      <svg width="16" height="18" viewBox="0 0 16 18" aria-hidden="true"><path d="M8 1a5 5 0 0 0-5 5c0 4 5 9 5 9s5-5 5-9a5 5 0 0 0-5-5z" fill="none" stroke="#fff" stroke-width="1.6"/><circle cx="8" cy="6" r="1.8" fill="#fff"/><path d="M2 17h12" stroke="#fff" stroke-width="1.4"/></svg>
    </div>
    <div class="venue-text">Harriet Colwin Theatre<br>Linden Ridge</div>
  </div>

  <div class="ticket-head">TICKETS CAN BE PURCHASED AT:</div>
  <div class="ticket-url">http://colwinstagehall.ticketnook.example/LEAPGLOWSPIN</div>
  <div class="or-divider">OR</div>
  <div class="call-line">By calling the ticket office at
    <svg width="14" height="14" viewBox="0 0 24 24" aria-hidden="true"><path d="M6.6 10.8a15 15 0 0 0 6.6 6.6l2.2-2.2a1 1 0 0 1 1-.25 11 11 0 0 0 3.6.6 1 1 0 0 1 1 1V20a1 1 0 0 1-1 1A17 17 0 0 1 3 4a1 1 0 0 1 1-1h3.5a1 1 0 0 1 1 1 11 11 0 0 0 .6 3.6 1 1 0 0 1-.25 1z" fill="#d0106c"/></svg>
    <span class="phone">(555) 555-PLAY</span>
  </div>
</section>

<section class="postcard postcard--back">
  <div class="back-panel"></div>
  <div class="ghost-photo" role="img" aria-label="Faded monochrome portrait of the headlining dancer"></div>
  <div class="pink-photo" role="img" aria-label="Headlining dancer standing in a bright pink dress"></div>
  <div class="back-title">
    <span><span class="initial blue">L</span>EAP</span>
    <span><span class="initial magenta">G</span>LOW</span>
    <span><span class="initial gold">S</span>PIN</span>
  </div>
  <p class="blurb">showcases the dance stylings of urban hip hop, ballet, modern jazz and much much more! Bay Area renown dancer/ choreographer Rosa Jean Fairbank headlines this cast of dancers and will amaze you as she takes you on a journey through dance that you will never forget. Join us for an experience that will prove to excite and delight you!</p>
  <div class="back-tickets">
    <div class="back-tickets-head">TICKETS CAN BE PURCHASED AT:</div>
    <div class="back-tickets-url">http://colwinstagehall.ticketnook.example/LEAPGLOWSPIN</div>
  </div>
  <div class="back-call">By calling the ticket office at</div>
  <div class="back-phone">
    <svg width="22" height="22" viewBox="0 0 24 24" aria-hidden="true"><path d="M6.6 10.8a15 15 0 0 0 6.6 6.6l2.2-2.2a1 1 0 0 1 1-.25 11 11 0 0 0 3.6.6 1 1 0 0 1 1 1V20a1 1 0 0 1-1 1A17 17 0 0 1 3 4a1 1 0 0 1 1-1h3.5a1 1 0 0 1 1 1 11 11 0 0 0 .6 3.6 1 1 0 0 1-.25 1z" fill="#d0106c"/></svg>
    (555) 555-PLAY
  </div>

  <div class="stamp-box"></div>
  <div class="address-line address-line--1"></div>
  <div class="address-line address-line--2"></div>
  <div class="address-line address-line--3"></div>
</section>

</body>
</html>
```